Oil and Gas Construction Company Brochure Design

We're redesigning our company Brochure. The easiest part about this...the layout, content, photos, etc. will follow our newly redesigned website:

www.bravelquorn.com

Thank you very much and please contact me should you have any questions!

Target Market(s)

Engineers, management, and operators in the oil field services

Industry/Entity Type

Oil And Gas

Requirements
Must have
• The same layout as the website, the same content, the same photos (ask me if you need anymore photos or if the layout your chose needs more)
• Also, follow the same color scheme as the website. Follow the same feel/mood as the website. Follow the same text as the website.

```html
<!DOCTYPE html>
<html lang="en">
<head>
<meta charset="utf-8">
<title>Bravelquorn Brochure – Inner Pages</title>
<link rel="stylesheet" href="https://fonts.googleapis.com/css2?family=Roboto:wght@300;400;700&display=swap">
<style>
:root{
  --bg:#3a3a3a;
  --paper:#f3f3f3;
  --panel-top:#d9d9d9;
  --panel-bottom:#c8c8c8;
  --bar:#b4b4b4;
  --teal:#2a88a8;
  --ink:#1e1e1e;
  --body:#3d3d3d;
  --muted:#6a6a6a;
}
*{box-sizing:border-box;margin:0;padding:0}
html,body{width:1200px;height:1200px;overflow:hidden;background:var(--bg);font-family:'Roboto',sans-serif;color:var(--body)}
.spread{position:absolute;left:80px;width:1040px;height:372px;display:flex;box-shadow:0 6px 18px rgba(0,0,0,.45)}
.spread--services{top:18px}
.spread--projects{top:408px}
.spread--management{top:798px}
.page{position:relative;width:520px;height:372px;background:var(--paper)}
.page--left{background:linear-gradient(90deg,var(--paper) 88%,#dcdcdc)}
.page--right{background:linear-gradient(90deg,#dcdcdc,var(--paper) 12%)}
.panel{position:absolute;left:16px;top:16px;right:16px;bottom:26px;background:linear-gradient(var(--panel-top),var(--panel-bottom))}
.header-bar{position:absolute;left:140px;right:18px;top:0;height:17px;background:linear-gradient(90deg,var(--bar),#cfcfcf)}
.header-tab{position:absolute;right:0;top:0;width:18px;height:17px;background:var(--teal)}
.section-title{position:absolute;left:7px;top:2px;font-weight:700;font-size:14px;color:var(--ink);letter-spacing:.2px}
.heading{font-weight:400;font-size:13px;color:var(--ink)}
.sub{font-size:8.5px;color:var(--body);margin:2px 0 4px}
.body{font-size:7px;line-height:1.5;font-weight:300;color:var(--body)}
.body p+p{margin-top:7px}
.photo{position:absolute}
.page-number{position:absolute;left:18px;bottom:9px;font-size:5px;color:var(--muted);letter-spacing:.3px}
.brand{position:absolute;right:18px;bottom:7px;display:flex;align-items:center;gap:3px;font-size:7.5px;font-weight:700;color:var(--ink)}
.brand::before{content:"";width:8px;height:8px;border-radius:50%;background:var(--ink)}
/* spread 1 */
.services{position:absolute;left:8px;top:32px;width:190px}
.services ul{margin-top:14px;list-style:none}
.services li{position:relative;padding-left:11px;font-size:7px;line-height:1.6;font-weight:300}
.services li::before{content:"•";position:absolute;left:2px}
.hse{position:absolute;left:238px;top:32px;right:8px}
.hse .body{margin-top:22px}
/* spread 2 */
.columns{position:absolute;left:4px;right:6px;top:146px;display:flex;gap:12px}
.columns .body{flex:1}
.map{position:absolute;left:0;right:0;top:22px;bottom:0}
/* spread 3 */
.bio{position:absolute;top:32px}
.bio .body{font-size:6.5px;line-height:1.45}
.bio .body p+p{margin-top:6px}
</style>
</head>
<body>

<section class="spread spread--services">
  <article class="page page--left">
    <div class="panel">
      <div class="header-bar"></div><div class="header-tab"></div>
      <div class="services">
        <h2 class="heading">I &amp; E Services</h2>
        <ul>
          <li>Plant Electrical Distribution &amp; System Installations</li>
          <li>Automation Systems Revamp / Upgrade Installations</li>
          <li>PLC &amp; DCS System Installations</li>
          <li>Control Panel Fabrication</li>
          <li>All Facets of Instrumentation Installations</li>
          <li>Lighting, Heat Tracing &amp; Facility Utility Service Installations</li>
          <li>Maintenance</li>
          <li>Electrical &amp; Instrumentation Testing Services</li>
          <li>Calibration Services</li>
          <li>Commissioning &amp; Start Up Services</li>
        </ul>
      </div>
      <div class="photo" role="img" aria-label="Row of grey electrical control cabinets inside a plant building" style="left:206px;top:32px;right:0;bottom:24px;background:linear-gradient(160deg,#8c949a,#b8bec2 45%,#7d8388)"></div>
    </div>
    <span class="page-number">PAGE # 8</span>
    <span class="brand">Bravelquorn</span>
  </article>
  <article class="page page--right">
    <div class="panel">
      <div class="header-bar"></div><div class="header-tab"></div>
      <h2 class="section-title">SAFETY</h2>
      <div class="photo" role="img" aria-label="Steel gas processing vessel and piping against a blue sky" style="left:0;top:32px;width:226px;bottom:24px;background:linear-gradient(175deg,#5b8fcf,#a9c3de 45%,#9aa1a6 60%,#6f757a)"></div>
      <div class="hse">
        <h2 class="heading">Health, Safety, &amp; Environmental</h2>
        <div class="body">
          <p>Bravelquorn Operations' success is a direct result of our committment to providing an "Injury Free" work environment where we operate all of our facilities and projects in a safe and efficient manner, and in compliance with all applicable health, safety and environmental regulations. Our goal is to provide a work environment where facilities and projects are free of recognized hazards; and people, equipment and the environment are not placed at risk of injury or damage.</p>
          <p>Bravelquorn's employees are our most vital asset. We care about every individual's safety and health. While quality and productivity are critical to our operations, they will never take precedence over the safety of personnel or protection of the environment.</p>
        </div>
      </div>
    </div>
    <span class="page-number">PAGE # 9</span>
    <span class="brand">Bravelquorn</span>
  </article>
</section>

<section class="spread spread--projects">
  <article class="page page--left">
    <div class="panel">
      <div class="header-tab"></div>
      <div class="photo" role="img" aria-label="Excavated red-soil foundation pit with rebar beside steel structures at a construction site" style="left:0;top:0;right:18px;height:138px;background:linear-gradient(180deg,#c9d3dc,#9a958e 35%,#c7805a 60%,#b0603c)"></div>
      <div class="columns">
        <div class="body"><p>Our management team holds itself responsible for recognizing, anticipating and analyzing the known and potential hazards of each project and to provide education, personal protective equipment (PPE) and leadership to eliminate those hazards and conditions at all construction sites. Our Health, Safety and Environmental Manual serves as an excellent tool for accident prevention.</p></div>
        <div class="body"><p>All Bravelquorn employees are trained to look for unsafe practices and conditions and correct the situation before it becomes a safety hazard. If an unsafe or hazardous condition arises during any work process, all Bravelquorn employees are empowered and encouraged to "stop work". Proper training, coupled with continuous communication between management and supervision ensures our capability to provide a safe working environment.</p></div>
        <div class="body"><p>Bravelquorn works closely with our customers to share awareness of one another's safety policies and procedures to maintain safety for all. All Bravelquorn employees are expected to follow these policies and procedures as well as provide input on how to improve them.</p><p>Safety is a priority for all Bravelquorn employees whether they are on or off the job site.</p></div>
      </div>
    </div>
    <span class="page-number">PAGE # 10</span>
    <span class="brand">Bravelquorn</span>
  </article>
  <article class="page page--right">
    <div class="panel">
      <div class="header-bar"></div><div class="header-tab"></div>
      <h2 class="section-title">PROJECTS</h2>
      <div class="map" role="img" aria-label="Map of the south-western United States and northern Mexico marking project locations across west Texas and south Texas" style="background:linear-gradient(135deg,#e9e4dc,#ddd6cb 50%,#e6e0d6)"></div>
    </div>
    <span class="page-number">PAGE # 11</span>
    <span class="brand">Bravelquorn</span>
  </article>
</section>

<section class="spread spread--management">
  <article class="page page--left">
    <div class="panel">
      <div class="header-bar"></div><div class="header-tab"></div>
      <h2 class="section-title">MANAGEMENT</h2>
      <div class="photo" role="img" aria-label="Aerial view of a gas plant yard with pipe racks and buildings" style="left:0;top:32px;width:152px;height:240px;background:linear-gradient(170deg,#9fb0bd,#b59c82 35%,#8a7e72 70%,#a08a74)"></div>
      <div class="bio" style="left:162px;right:8px">
        <h2 class="heading">Dale Fenwright</h2>
        <div class="sub">President &amp; Founder</div>
        <div class="body">
          <p>Mr. Fenwright has over 40 years of project development and management experience in the engineering and construction for the natural gas and petrochemical industries.</p>
          <p>He began his career in 1974 with Harlow Electric Co. Inc. In 1989 Mr. Fenwright served as General Manager for Harlow Electric Co. Inc. In 1996 he was promoted to Vice President of Operations for Harlow Industries Inc., where he was responsible for the operations of Harlow Electric Co. Inc., Harcon Inc., and Harlow Engineering and Construction Inc.</p>
          <p>His responsibilities included overseeing management personnel, safety, planning, forecasting, growth analysis, market assessments and maintaining the quality and profitability of all entities. From 2008 to 2010, Mr. Fenwright served as Chief Operating Officer for Harlow Industries, Inc. During his tenure, the Harlow companies experienced significant growth and expanded into numerous markets and opened two new regional offices.</p>
          <p>In 2000, Mr. Fenwright Co-founded and became Vice President of Meridel Gas Services, LLC, a contract gas treating company that was later sold to Ridgeline Energy Services, L.P. (NASDAQ: RDGX) in 2003.</p>
        </div>
      </div>
    </div>
    <span class="page-number">PAGE # 12</span>
    <span class="brand">Bravelquorn</span>
  </article>
  <article class="page page--right">
    <div class="panel">
      <div class="header-bar"></div><div class="header-tab"></div>
      <div class="bio" style="left:8px;right:168px">
        <h2 class="heading">Owen Fenwright</h2>
        <div class="sub">Vice President of Bravelquorn Constructors, Ltd.</div>
        <div class="body">
          <p>Mr. Fenwright has over 20 years of experience in providing heavy industrial electrical and general construction installations to the natural gas and petrochemical industries. He has managed and overseen major projects, such as cogeneration plants, compressor station installations, CO2 plant installations and relocations, grass roots amine plant installations, general maintenance projects and capital projects in the Oil &amp; Gas industry.</p>
          <p>Mr. Fenwright is directly responsible for all operational aspects of Bravelquorn Constructors, LTD, where he applies the importance of safety, quality, management, and cost control in all day to day activities.</p>
          <p>Prior to beginning his career in the Oil and Gas industry, Mr. Fenwright served in the United States Army as a Medical Specialist. During his service, Mr. Fenwright was deployed to Bosnia during Operation Joint Guard and Operation Joint Forge.</p>
          <p>Mr. Fenwright holds construction licenses in New Mexico and Oklahoma.</p>
        </div>
      </div>
      <div class="photo" role="img" aria-label="Cable tray bundle and steel stairway on an outdoor plant structure" style="right:0;top:32px;width:156px;height:240px;background:linear-gradient(175deg,#7ea6cf,#b2c3d2 40%,#8d969c 70%,#6e767c)"></div>
    </div>
    <span class="page-number">PAGE # 13</span>
    <span class="brand">Bravelquorn</span>
  </article>
</section>

</body>
</html>
```